Half page print ad for magazine

Hi PixelGuild community !

We need you once more :-) Our current logo was designed by one of you !

We need a half page print ad for a magazine with the following specifications :
H139.59 mm * W197.4 mm
Bleed: 3mm on all sides
Resolution: 300 dpi minimum
Format: PDF/X-1a:2001 format
Colour: CMYK

We are a company specializing in internships abroad. For this ad the target is British companies looking for French interns.
We want something simple, little text and a symbolic link between the graphic and textual elements of the ad. If you have a look at our profile image on Chatterbook, we chose a skyline of skyscrapers with various shapes to illustrate our slogan : Diversify your experience.
The idea here is to create a new catchphrase that would make the link with the new design aiming at British companies.
Our recruiting services are free for companies and that should also be clear in the ad.

I'd be happy to provide further information. I have attached our logo and a sample of 3 ads (OK they're full-page and we need a half one...) with more or less text. We'd really like to see real people on it, unless you come up with a better idea.

I look forward to sharing with you.

Kind regards,

Laurent
Marketing and Community Manager, TrainaboardNow

Hello PG designers, Thanks for answering our invitation for that half-page print ad. We are about to select the design, so please do not send us any new mock-ups, as we won't be able to consider them anymore. We appreciate all your work and your answers regarding that project. Best regards, TrainAboardNow

Target Market(s)

British companies looking for French interns

Industry/Entity Type

It Company

Font styles to use
Serif
Sans Serif

Requirements
Must have
• 1. Picture of a person or people.

2. Catchphrase : Make the most of a unique free service to recruit French interns

3 Make "free service" stand out in a different color

4 At the bottom of the ad, add:
Want to know more ?
contact@trainaboardnow.example
+33 400 555 012
www.trainaboardnow.example

```html
<!DOCTYPE html>
<html lang="en">
<head>
<meta charset="utf-8">
<title>TrainAboardNow – Half Page Ad</title>
<link href="https://fonts.googleapis.com/css2?family=Didact+Gothic&family=Tinos&display=swap" rel="stylesheet">
<style>
  :root {
    --brand-blue: #1b7cc4;
    --text-dark: #3a3a3a;
    --text-mid: #4a4a4a;
    --paper: #ffffff;
    --photo-light: #eef0f2;
    --photo-mid: #8c8f95;
    --photo-dark: #4b4e55;
    --bar-shadow: rgba(0, 0, 0, 0.18);
  }
  html, body {
    margin: 0;
    padding: 0;
    width: 1200px;
    height: 849px;
    overflow: hidden;
    background: var(--paper);
  }
  .ad {
    position: relative;
    width: 1200px;
    height: 849px;
    background: var(--paper);
    font-family: "Didact Gothic", "Century Gothic", sans-serif;
    overflow: hidden;
  }
  .people-photo {
    position: absolute;
    left: 62px;
    top: 147px;
    width: 594px;
    height: 583px;
    background: radial-gradient(ellipse at 50% 55%, var(--photo-mid) 0%, var(--photo-dark) 45%, var(--photo-light) 75%, var(--paper) 100%);
  }
  .catchphrase {
    position: absolute;
    left: 690px;
    top: 128px;
    width: 420px;
    text-align: center;
    color: var(--text-dark);
    font-size: 29px;
    line-height: 35px;
    margin: 0;
    font-weight: 400;
  }
  .catchphrase .highlight {
    display: block;
    color: var(--brand-blue);
    font-size: 31px;
    letter-spacing: 0.5px;
  }
  .more-info {
    position: absolute;
    left: 700px;
    top: 475px;
    width: 428px;
    text-align: center;
    margin: 0;
    font-family: "Tinos", "Times New Roman", serif;
    font-size: 27px;
    color: var(--brand-blue);
    letter-spacing: 0.5px;
  }
  .contact-bar {
    position: absolute;
    left: 0;
    top: 730px;
    width: 1200px;
    height: 119px;
    background: var(--paper);
    box-shadow: 0 -10px 18px var(--bar-shadow);
  }
  .contact-list {
    position: absolute;
    right: 726px;
    top: 16px;
    margin: 0;
    padding: 0;
    list-style: none;
    text-align: right;
    font-size: 23px;
    line-height: 29px;
    color: var(--text-mid);
  }
  .pointer-icon {
    position: absolute;
    left: 490px;
    top: 21px;
  }
  .brand {
    position: absolute;
    left: 570px;
    top: 30px;
    display: flex;
    align-items: center;
    gap: 22px;
  }
  .brand-dot {
    width: 70px;
    height: 70px;
    border-radius: 50%;
    background: var(--brand-blue);
  }
  .brand-name {
    font-size: 50px;
    color: var(--text-dark);
    line-height: 1;
  }
</style>
</head>
<body>
  <main class="ad">
    <div class="people-photo" role="img" aria-label="Photo of a smiling businesswoman and businessman in grey suits standing back to back with arms crossed"></div>

    <h1 class="catchphrase">
      Make the most of a
      <span class="highlight">UNIQUE FREE SERVICE</span>
      to recruit your French interns.
    </h1>

    <p class="more-info">WANT TO KNOW MORE ?</p>

    <footer class="contact-bar">
      <ul class="contact-list">
        <li>contact@trainaboardnow.example</li>
        <li>+33 400 555 012</li>
        <li>www.trainaboardnow.example</li>
      </ul>
      <svg class="pointer-icon" width="28" height="28" viewBox="0 0 28 28" aria-hidden="true">
        <circle cx="14" cy="14" r="14" fill="var(--brand-blue)"/>
        <polygon points="8,14 17,8 17,20" fill="#ffffff"/>
      </svg>
      <div class="brand">
        <span class="brand-dot" aria-hidden="true"></span>
        <span class="brand-name">TrainAboardNow</span>
      </div>
    </footer>
  </main>
</body>
</html>
```